I am a Vantrell Service and Marketing Consultant looking for a Vantrellesque but business like cover wit

I need a bookcover designed for my new business book titled; "Orderly Wonder. 7 Bright Doors To Vantrellize Your Firm. Outshine, Outlast & Outgrow Your Rivals in EVERY Climate"

The name of my company is Harbor Care Today

We work with companies to implement Vantrell Style Service and Themeing, and then create marketing campaigns to promote that level of service.

I have used Owl Whisper font in the past, but am not tied to it

Target Market(s)

Small Business owners, medical practices, law firms

Industry/Entity Type

Business

Requirements
Must have
• Colors: RGB 30, 54, 128 AND 113, 191, 76. These are the two colors in my logo, if you need it.
Nice to have
• Magic Key?? Gloved Hand (similar to a Vantrell Character)??
Should not have
• Any copyright protected inages

```html
<!DOCTYPE html>
<html lang="en">
<head>
<meta charset="UTF-8">
<title>Orderly Wonder — Book Cover</title>
<link rel="stylesheet" href="https://fonts.googleapis.com/css2?family=Francois+One&family=Arimo:wght@400;700&family=Tinos:ital,wght@1,400;1,700&display=swap">
<style>
  :root {
    --navy: rgb(30, 54, 128);
    --navy-light: #41609e;
    --green: rgb(113, 191, 76);
    --green-light: #8fd06a;
    --white: #ffffff;
    --paper: #ffffff;
    --gold: #c9a227;
    --gold-light: #e3c15a;
    --glove: #e9eef6;
  }
  html, body {
    margin: 0;
    padding: 0;
    width: 1200px;
    height: 1200px;
    overflow: hidden;
    background: var(--paper);
  }
  .canvas {
    position: relative;
    width: 1200px;
    height: 1200px;
  }
  .cover {
    position: absolute;
    left: 280px;
    top: 150px;
    width: 640px;
    height: 900px;
    background: linear-gradient(90deg, var(--navy) 0%, var(--navy) 55%, var(--navy-light) 100%);
    overflow: hidden;
    box-shadow: 0 10px 30px rgba(0,0,0,0.18);
  }
  .publisher-mark {
    position: absolute;
    top: 70px;
    left: 0;
    width: 100%;
    display: flex;
    justify-content: center;
    align-items: center;
    gap: 12px;
  }
  .publisher-dot {
    width: 22px;
    height: 22px;
    border-radius: 50%;
    background: var(--white);
  }
  .publisher-name {
    font-family: "Arimo", sans-serif;
    font-weight: 400;
    font-size: 30px;
    color: var(--green);
    letter-spacing: 0.5px;
  }
  .title {
    position: absolute;
    margin: 0;
    font-family: "Francois One", sans-serif;
    font-weight: 400;
    line-height: 1;
    white-space: nowrap;
  }
  .title-top {
    top: 200px;
    left: 110px;
    font-size: 118px;
    color: var(--white);
    letter-spacing: -1px;
  }
  .title-bottom {
    top: 318px;
    left: 80px;
    font-size: 124px;
    color: var(--green);
    letter-spacing: -1px;
  }
  .key-art {
    position: absolute;
    top: 130px;
    left: 525px;
    width: 44px;
    height: 200px;
    border-radius: 22px;
    background: linear-gradient(180deg, var(--gold-light), var(--gold));
  }
  .glove-art {
    position: absolute;
    top: 370px;
    left: 468px;
    width: 150px;
    height: 240px;
    border-radius: 45% 40% 35% 50%;
    background: linear-gradient(135deg, var(--white), var(--glove));
  }
  .subtitle {
    position: absolute;
    top: 650px;
    left: 0;
    width: 100%;
    text-align: center;
    font-family: "Tinos", serif;
    font-style: italic;
    color: var(--white);
  }
  .subtitle-lead {
    font-size: 27px;
    margin: 0 0 8px;
  }
  .subtitle-rule {
    width: 440px;
    height: 1px;
    margin: 0 auto 8px;
    background: var(--green);
  }
  .subtitle-promise {
    font-size: 25px;
    line-height: 1.2;
    margin: 0;
  }
  .subtitle-promise strong {
    font-weight: 700;
  }
  .author-band {
    position: absolute;
    left: 0;
    top: 790px;
    width: 100%;
    height: 90px;
    background: linear-gradient(90deg, var(--green), var(--green-light));
    display: flex;
    align-items: center;
    justify-content: center;
  }
  .author-name {
    font-family: "Arimo", sans-serif;
    font-weight: 400;
    font-size: 52px;
    color: var(--white);
    letter-spacing: 1px;
  }
</style>
</head>
<body>
  <main class="canvas">
    <section class="cover">
      <div class="publisher-mark">
        <span class="publisher-dot"></span>
        <span class="publisher-name">Harbor Care Today Institute</span>
      </div>

      <h1 class="title title-top">Orderly</h1>
      <div class="key-art" role="img" aria-label="Ornate golden key hanging beside the title"></div>
      <h1 class="title title-bottom">Wonder</h1>
      <div class="glove-art" role="img" aria-label="White-gloved hand reaching out in a welcoming gesture"></div>

      <div class="subtitle">
        <p class="subtitle-lead">7 Bright Doors To Vantrellize Your Firm</p>
        <div class="subtitle-rule"></div>
        <p class="subtitle-promise">Outshine, Outlast &amp; Outgrow<br>Your Rivals in <strong>EVERY</strong> Climate</p>
      </div>

      <div class="author-band">
        <span class="author-name">REED CALLOWAY</span>
      </div>
    </section>
  </main>
</body>
</html>
```